Travel Health Brief Beautiful and Simple PDF design showing risks on your travels

Please see the attached PDF named "Compass Trek Health Brief", and the document for the full brief for tis work.
This document is a summary of a traveller's planned trip itinerary and any associated health risks from diseases and the related vaccines available. It is available for purchase once the traveller has provided us with information about their trip.
Although this document contains all the required content and the correct colour scheme, its design needs to be of a quality that reflects its purchase price. It would benefit from looking more attractive and for its data to be laid out in a way to make it more easily readable.

Target Market
Individuals, families and professionals looking to plan international travel.

Deliverables
The project will deliver a new design for the PDF in vector format (preferably a layered AI file), along with individual vector files for any illustrations created for the project.

Design Overview
This document will be displayed onscreen in HTML format so the design needs to work well for both print and web.
The design must follow the attached Compass Trek Health brand book, we like the colour scheme we have and do not wish to digress too much from this.
The use of appropriate illustration and iconography is encouraged. These can add additional colours so long as these are complementary to the existing palette.
We will be looking for:
● Attractive layout
● Appropriate illustration
● Good use of whitespace
● Good choice of font size to denote information hierarchy
● Recognisably the same branding as the current sample document provided

Specific Notes on Content
The Your Trip section could contain 1 destination or many. The design must accommodate any number of destinations. It should be optimised to look best for trips of 1 to 3 destinations.
The design of the map pins cannot change.
The map is a static google map and will be using the colour scheme and map pins displayed.
This map can be a maximum image size of 640 x 640 pixels, but this can be stretched in the PDF - however if it's too big it will look blurry so the size it is now is about perfect.
One idea we have had is to include infographic summary data on the first page below the map/itinerary. Perhaps counts for each disease risk category.
The colours we have chosen for each disease risk category are not set in stone, but we want to avoid any sort of traffic light (red/amber/green) colours. You are welcome to stick with the existing colours.
The number of diseases in each section is completely dynamic. There could be, none, one or many, so the design needs to accommodate that without being too linear and boring a layout, like it is at the moment.
The example we've provided purposefully includes most of the diseases in question so you can see what the content looks like for each one.
The hyperlinks could theoretically be any length. We have left them as URLs rather than link text as the PDF document needs to be printable. In the onscreen version we use link text.
Updates

Target Market(s)

Individual travellers researching the risk of foreign travel

Industry/Entity Type

Healthcare, travel

Requirements
Must have
• See brief
Nice to have
• See brief

```html
<!DOCTYPE html>
<html lang="en">
<head>
<meta charset="utf-8">
<title>Compass Travel Health Brief</title>
<link rel="stylesheet" href="https://fonts.googleapis.com/css2?family=Inter:wght@300;400;500;600;700;800&display=swap">
<style>
  :root {
    --navy: #1b2a4e;
    --ink: #111418;
    --teal: #1a6a94;
    --sky: #1aa0db;
    --ocean: #2a91c4;
    --light: #5ab0d8;
    --map: #a3cde6;
    --card: #e8f4fa;
    --rule: #cfe4f0;
    --grey: #7a7f86;
    --text: #3b4a63;
  }
  * { margin: 0; padding: 0; box-sizing: border-box; }
  html, body { width: 848px; height: 1200px; overflow: hidden; background: #fff; }
  body { font-family: "Inter", Arial, sans-serif; color: var(--navy); }
  .page { position: relative; width: 848px; height: 1200px; overflow: hidden; background: #fff; }
  .hero { position: absolute; left: 0; top: 0; width: 848px; height: 620px; }
  .hero-title { position: absolute; left: 600px; width: 222px; top: 432px; text-align: center; color: #fff; }
  .hero-title .big { font-size: 21px; font-weight: 600; line-height: 29px; letter-spacing: 0.3px; }
  .hero-title .for { font-size: 11px; font-weight: 400; margin-top: 4px; }
  .hero-title .trip { font-size: 15px; font-weight: 500; margin-top: 5px; }

  .brand-title { position: absolute; left: 54px; top: 622px; }
  .brand-title .name { font-size: 31px; font-weight: 700; letter-spacing: 3.5px; line-height: 36px; }
  .brand-title .sub { font-size: 28px; font-weight: 500; line-height: 36px; }

  .trip-card { position: absolute; left: 53px; top: 719px; width: 316px; height: 412px; border-radius: 30px; background: var(--card); padding: 26px 0 0 31px; }
  .traveller { font-size: 22px; font-weight: 400; color: var(--light); line-height: 26px; }
  .trip-heading { font-size: 33px; font-weight: 700; line-height: 40px; margin-top: 2px; }
  .loc-heading { font-size: 20px; font-weight: 500; margin-top: 10px; }
  .stops { list-style: none; margin-top: 10px; }
  .stop { position: relative; padding-left: 33px; height: 58.5px; }
  .stop svg { position: absolute; left: 0; top: 6px; }
  .stop .place { font-size: 18px; font-weight: 400; color: var(--text); line-height: 22px; }
  .stop .date { font-size: 12px; color: var(--grey); margin-top: 3px; }
  .totals { margin-top: 12px; font-size: 15px; font-weight: 300; color: var(--grey); line-height: 23.5px; }

  .risk-heading { position: absolute; left: 470px; width: 284px; top: 624px; text-align: center; font-size: 25px; line-height: 30px; font-weight: 600; color: var(--ink); white-space: nowrap; }
  .risk-path { position: absolute; left: 0; top: 0; }
  .badge { position: absolute; width: 64px; height: 64px; border-radius: 50%; color: #fff; font-size: 23px; font-weight: 400; display: flex; align-items: center; justify-content: center; box-shadow: 0 0 0 4px #fff, 0 0 0 6px #e4eef4; }
  .badge-1 { left: 579px; top: 685px; background: var(--teal); }
  .badge-2 { left: 579px; top: 780px; background: var(--sky); }
  .badge-3 { left: 579px; top: 875px; background: var(--ocean); }
  .badge-4 { left: 579px; top: 969px; background: var(--light); }

  .cat { position: absolute; }
  .cat .label { font-size: 12.5px; font-weight: 500; letter-spacing: 0.4px; color: var(--navy); line-height: 15px; white-space: nowrap; }
  .cat .rule { height: 3px; background: var(--rule); border-radius: 2px; margin-top: 6px; }
  .cat ul { list-style: none; margin-top: 6px; font-size: 10.5px; font-weight: 400; color: var(--grey); line-height: 14px; letter-spacing: 0.2px; white-space: nowrap; }
  .cat-right { left: 682px; }
  .cat-left { right: 308px; text-align: right; }
  .cat-left .rule { margin-left: auto; }
  .cat-mandatory { top: 709px; }
  .cat-mandatory .rule { width: 70px; }
  .cat-recommended { top: 803px; }
  .cat-recommended .rule { width: 89px; }
  .cat-consider { top: 900px; }
  .cat-consider .rule { width: 113px; }
  .cat-other { top: 990px; }
  .cat-other .rule { width: 94px; }

  .brand-mark { position: absolute; left: 656px; top: 1101px; display: flex; align-items: center; gap: 7px; font-size: 13px; font-weight: 600; color: var(--navy); white-space: nowrap; }
  .brand-mark .dot { width: 16px; height: 16px; border-radius: 50%; background: var(--teal); }

  .footer { position: absolute; left: 0; top: 1148px; width: 848px; height: 52px; background: linear-gradient(90deg, var(--light) 0%, #3a6a93 45%, var(--navy) 100%); }
  .footer-text { position: absolute; left: 30px; top: 19px; font-size: 13px; font-weight: 400; color: #fff; letter-spacing: 0.5px; }
  .footer-swoosh { position: absolute; right: 0; top: -15px; }
</style>
</head>
<body>
<main class="page">
  <svg class="hero" width="848" height="620" viewBox="0 0 848 620">
    <defs>
      <linearGradient id="bandFill" x1="0" y1="0" x2="1" y2="0">
        <stop offset="0" stop-color="#5ab0d8"/>
        <stop offset="0.6" stop-color="#30587f"/>
        <stop offset="1" stop-color="#1b2a4e"/>
      </linearGradient>
      <linearGradient id="mapFill" x1="0" y1="0" x2="1" y2="1">
        <stop offset="0" stop-color="#eef6fa"/>
        <stop offset="0.45" stop-color="#d9ecf3"/>
        <stop offset="0.7" stop-color="#a3cde6"/>
        <stop offset="1" stop-color="#94c5e2"/>
      </linearGradient>
    </defs>
    <path class="hero-band" d="M0,402 L0,440 L300,617 Q338,640 378,617 L848,352 V262 Z" fill="url(#bandFill)"/>
    <path class="hero-map" role="img" aria-label="Static route map of Africa marking Luanda, Nairobi and Kampala" d="M0,0 H848 V268 L378,556 Q338,580 298,556 L0,402 Z" fill="url(#mapFill)"/>
    <g class="map-pins" fill="#5ab0d8">
      <g transform="translate(212,256)">
        <path d="M0,28 C-4,20 -17,12 -17,0 A17,17 0 1 1 17,0 C17,12 4,20 0,28 Z"/>
        <text x="0" y="6" text-anchor="middle" fill="#fff" font-family="Inter, sans-serif" font-size="16">1</text>
      </g>
      <g transform="translate(385,174)">
        <path d="M0,28 C-4,20 -17,12 -17,0 A17,17 0 1 1 17,0 C17,12 4,20 0,28 Z"/>
        <text x="0" y="6" text-anchor="middle" fill="#fff" font-family="Inter, sans-serif" font-size="16">3</text>
      </g>
      <g transform="translate(423,189)">
        <path d="M0,28 C-4,20 -17,12 -17,0 A17,17 0 1 1 17,0 C17,12 4,20 0,28 Z"/>
        <text x="0" y="6" text-anchor="middle" fill="#fff" font-family="Inter, sans-serif" font-size="16">2</text>
      </g>
    </g>
    <path class="hero-panel" d="M502,465 L688,361 L848,445 V528 L745,583 Q706,604 667,583 Z" fill="#1b2a4e"/>
    <path d="M688,361 L744,329 L848,386 V445 Z" fill="#5ab0d8"/>
    <path d="M744,329 L780,309 L848,346 V386 Z" fill="#1a6a94"/>
    <path d="M780,309 L848,268 V346 Z" fill="#1b2a4e"/>
    <circle cx="808" cy="336" r="2" fill="#cfe4f0"/>
  </svg>
  <div class="hero-title">
    <div class="big">DISEASE RISKS<br>&amp; VACCINES</div>
    <div class="for">FOR</div>
    <div class="trip">YOUR TRIP</div>
  </div>

  <header class="brand-title">
    <div class="name">COMPASS</div>
    <div class="sub">Travel Health Brief</div>
  </header>

  <section class="trip-card">
    <div class="traveller">Mara Quill</div>
    <h1 class="trip-heading">Your Trip</h1>
    <h2 class="loc-heading">Locations</h2>
    <ol class="stops">
      <li class="stop">
        <svg width="20" height="32" viewBox="0 0 20 32"><path d="M10,24 C7,19 1,15 1,10 A9,9 0 1 1 19,10 C19,15 13,19 10,24 Z" fill="#1a6a94"/><circle cx="10" cy="10" r="6" fill="#fff"/><text x="10" y="13" text-anchor="middle" font-size="8" fill="#1b2a4e" font-family="Inter, sans-serif">1</text><circle cx="10" cy="30" r="1.5" fill="#1a6a94"/></svg>
        <div class="place">Luanda, Angola</div>
        <div class="date">On 17 Aug, 2023</div>
      </li>
      <li class="stop">
        <svg width="20" height="32" viewBox="0 0 20 32"><path d="M10,24 C7,19 1,15 1,10 A9,9 0 1 1 19,10 C19,15 13,19 10,24 Z" fill="#1a6a94"/><circle cx="10" cy="10" r="6" fill="#fff"/><text x="10" y="13" text-anchor="middle" font-size="8" fill="#1b2a4e" font-family="Inter, sans-serif">2</text><circle cx="10" cy="30" r="1.5" fill="#1a6a94"/></svg>
        <div class="place">Neirboi, Kenya</div>
        <div class="date">On 17 Aug, 2023</div>
      </li>
      <li class="stop">
        <svg width="20" height="32" viewBox="0 0 20 32"><path d="M10,24 C7,19 1,15 1,10 A9,9 0 1 1 19,10 C19,15 13,19 10,24 Z" fill="#1a6a94"/><circle cx="10" cy="10" r="6" fill="#fff"/><text x="10" y="13" text-anchor="middle" font-size="8" fill="#1b2a4e" font-family="Inter, sans-serif">3</text><circle cx="10" cy="30" r="1.5" fill="#1a6a94"/></svg>
        <div class="place">Kampala, Uganda</div>
        <div class="date">On 17 Aug, 2023</div>
      </li>
    </ol>
    <div class="totals">
      Total Days: 15<br>
      Return Date: 31 Aug, 2023<br>
      Report Date: 20 Jul 2023, 16:2615
    </div>
  </section>

  <h2 class="risk-heading">RISK CATEGORIES</h2>
  <svg class="risk-path" width="848" height="1200" viewBox="0 0 848 1200">
    <path d="M609,670 A47,47 0 0 0 611,764 A48,48 0 0 1 611,860 A48,48 0 0 0 611,955 A47,47 0 0 1 609,1048" fill="none" stroke="#d6e9f3" stroke-width="2.5" stroke-linecap="round"/>
  </svg>
  <div class="badge badge-1">01</div>
  <div class="badge badge-2">02</div>
  <div class="badge badge-3">03</div>
  <div class="badge badge-4">04</div>

  <div class="cat cat-right cat-mandatory">
    <div class="label">MENDATORY</div>
    <div class="rule"></div>
    <ul><li>Yellow fever</li></ul>
  </div>
  <div class="cat cat-left cat-recommended">
    <div class="label">RECOMMENDED</div>
    <div class="rule"></div>
    <ul>
      <li>Rabies</li><li>Polio</li><li>Malaria</li><li>Hepatitis B</li><li>Hepatitis A</li><li>Typhoid Fever</li>
    </ul>
  </div>
  <div class="cat cat-right cat-consider">
    <div class="label">TO BE CONSIDERED</div>
    <div class="rule"></div>
    <ul><li>Meningococcal Disease</li></ul>
  </div>
  <div class="cat cat-left cat-other">
    <div class="label">OTHER DISEASES</div>
    <div class="rule"></div>
    <ul>
      <li>HIV</li><li>Dengue</li><li>Chikungunya</li><li>Zika</li><li>African Trypanosomiasis</li><li>African Tick-Bite Fever</li><li>Tuberclosis(TB)</li>
    </ul>
  </div>

  <div class="brand-mark"><span class="dot"></span>Compass Trek Health</div>

  <footer class="footer">
    <div class="footer-text">COMPASS TREK HEALTH BRIEF</div>
    <svg class="footer-swoosh" width="140" height="67" viewBox="0 0 140 67">
      <path d="M10,67 L70,25 Q90,12 110,8 L140,2 V67 Z" fill="#1a6a94"/>
      <path d="M45,67 L95,25 Q115,8 140,5 V67 Z" fill="#1b2a4e"/>
    </svg>
  </footer>
</main>
</body>
</html>
```